Corvane Capital LLC
I need single sided standard sized Business Card [3.5" x 2"]
Fonts to be determined by designer
Professional
Derek Halloway
Chairman
Kestrel Hall Tower
418 North Larkin Avenue
Los Angeles, CA 90099
555.014.2739 X1
Acquisitions@Corvane-Capital.net
http://www.Corvane-Capital.net
We want to see what designs are out there for a cutting edge business card that shows off our 3 main goals: Intense - Expressive - Important . The business card can be vertical or horizontal, can use fonts of the designer's choice and be relatively "unique". More than just a simple black on white business card.
Use the logo and CORVANE but you do not need to use the blue background if your design does not warrant it. Financial LLC can be in any font you desire if it matches your design

```html
<!DOCTYPE html>
<html lang="en">
<head>
<meta charset="utf-8">
<title>Corvane Capital LLC — Business Card</title>
<link rel="stylesheet" href="https://fonts.googleapis.com/css2?family=Source+Sans+3:wght@400;600;700&display=swap">
<style>
  :root {
    --backdrop: #4a2012;
    --card: #ffffff;
    --brand-brown: #7a3f1c;
    --name-brown: #7a4a22;
    --label-gold: #c7831c;
    --ink: #2b2b2b;
    --divider: #6a5a4a;
    --band-dark: #3a2a1a;
    --gold-light: #e9c25a;
    --gold-mid: #c99a2e;
    --gold-dark: #8a6418;
    --mark: #2a2f3a;
  }
  * { margin: 0; padding: 0; box-sizing: border-box; }
  html, body {
    width: 1200px; height: 965px; overflow: hidden;
    background: var(--backdrop);
    font-family: "Source Sans 3", "Myriad Pro", sans-serif;
  }
  .card {
    position: absolute; left: 150px; top: 225px;
    width: 900px; height: 514px;
    background: var(--card);
    border-radius: 26px;
    overflow: hidden;
    box-shadow: 0 10px 28px rgba(0,0,0,0.35);
  }
  .brand {
    position: absolute; left: 40px; top: 110px; width: 290px;
    display: flex; flex-direction: column; align-items: center;
    color: var(--brand-brown); font-weight: 600;
  }
  .brand-mark {
    width: 150px; height: 150px;
    background: var(--mark);
    margin-bottom: 24px;
  }
  .brand-name { font-size: 80px; line-height: 0.9; letter-spacing: 1px; }
  .brand-sub { font-size: 19px; letter-spacing: 9px; margin-top: 6px; text-transform: uppercase; }
  .divider {
    position: absolute; left: 368px; top: 96px;
    width: 2px; height: 198px; background: var(--divider);
  }
  .contact { position: absolute; left: 396px; top: 96px; color: var(--ink); }
  .contact-name { font-size: 33px; font-weight: 600; color: var(--name-brown); line-height: 1.15; }
  .contact-title { font-size: 27px; line-height: 1.2; margin-bottom: 24px; }
  .contact-lines { list-style: none; font-size: 24px; line-height: 34px; }
  .label { color: var(--label-gold); font-weight: 700; }
  .rule {
    position: absolute; left: 0; right: 0; top: 470px;
    height: 4px; background: var(--band-dark);
  }
  .band {
    position: absolute; left: 0; right: 0; top: 474px; bottom: 0;
    background: linear-gradient(180deg, var(--gold-light) 0%, var(--gold-mid) 45%, var(--gold-dark) 100%);
  }
</style>
</head>
<body>
  <article class="card">
    <div class="brand">
      <div class="brand-mark"></div>
      <div class="brand-name">CORVANE</div>
      <div class="brand-sub">Capital LLC</div>
    </div>
    <div class="divider"></div>
    <section class="contact">
      <h1 class="contact-name">Derek Halloway</h1>
      <p class="contact-title">Chairman</p>
      <ul class="contact-lines">
        <li>Kestrel Hall Tower</li>
        <li>418 North Larkin Avenue</li>
        <li>Los Angeles, CA 90099</li>
        <li><span class="label">Phone</span> : 555.014.2739 X1</li>
        <li><span class="label">Fax</span> : 555.019.4406</li>
        <li><span class="label">Email</span> : Acquisitions@Corvane-Capital.net</li>
        <li><span class="label">Web</span> : http://www.Corvane-Capital.net</li>
      </ul>
    </section>
    <div class="rule"></div>
    <div class="band"></div>
  </article>
</body>
</html>
```